Cleaning Service Company In need of Good Web presence.

The company is a cleaning service company which provides professional staff and service for cleaning. This is a project to build a site that is both solid and a strong recognition of our organization. It is supposed to show quality, cleanliness, professionalism. The use of images and art for imagery is all good just to have a site that is consistent and solid. There might be a chance to make stationary, logo and business cars if someone feels they can build a brand that is consistent. The image we are going for is clean solid and to stand out. Finally stationary should not be expensive to print.

Current logo is attached and can be used or can be made more creative.

Target Market(s)

Corporate and Government entities, that will feel that this company has a brand that sets it apart from the rest. The company is new so the modification of the logo will not be an issue if a more solid brand come out of this project. The idea is to have a clean consistent product that stands our from others in terms of website, stationary, etc

Industry/Entity Type

Cleaning Service

Contact Information for Business Card

P.O.Box 41967
Riffa
Kingdom of Bahrain

Logo Text

Maple Ridge Solutions

Number of Pages Required

4 page

Font styles to use
Sans Serif

Colors
abd036
cadf82
eaf2ce
9bcb3b

Requirements
Must have
• Green Color to be used in order to stick to the name. Also the creativity and boldness in an elegant manner.
Nice to have
• Arabic name of company
• نوفا بلو للحلول ذ.م.م
• if cannot be put at least make a location should be chosen
• Also could be a bit of 3D given to the logo if it could stay elegent.
Should not have
• Should not show people cleaning.

```html
<!DOCTYPE html>
<html lang="en">
<head>
<meta charset="utf-8">
<title>Maple Ridge Solutions — Cleaning Services</title>
<link href="https://fonts.googleapis.com/css2?family=Open+Sans:wght@400;600;700&family=Raleway:wght@400;500;600&display=swap" rel="stylesheet">
<style>
:root{
  --green:#9bcb3b;
  --green-bright:#abd036;
  --green-dark:#0d6b38;
  --green-line:#cadf82;
  --ink:#222;
  --text:#555;
  --muted:#888;
  --panel:#eef1f4;
  --border:#d9dde1;
  --white:#fff;
}
*{margin:0;padding:0;box-sizing:border-box}
html,body{width:1200px;height:2917px;overflow:hidden}
body{position:relative;background:var(--white);font-family:"Open Sans",sans-serif;color:var(--ink)}
.abs{position:absolute}

/* top strip */
.top-strip{left:0;top:0;width:1200px;height:31px;background:var(--green)}
.social-top{right:98px;top:8px;display:flex;gap:16px}
.social-top span{width:12px;height:12px;border-radius:50%;background:var(--white);opacity:.9}

/* header */
.brand{left:100px;top:30px;display:flex;align-items:center;gap:10px;width:260px}
.brand-mark{width:48px;height:48px;border-radius:50%;background:var(--green);flex:none}
.brand-name{font-weight:700;font-size:17px;line-height:1.15;color:var(--green-dark)}
.contact{display:flex;align-items:center;gap:14px;top:66px}
.contact svg{width:26px;height:26px}
.contact small{display:block;font-size:12px;color:var(--muted)}
.contact b{display:block;font-size:14px;font-weight:600;color:var(--ink)}
.contact.email{left:545px}
.contact.call{left:770px}
.btn{display:flex;align-items:center;justify-content:center;font-weight:700;font-size:14px;color:var(--white);text-transform:uppercase}
.btn-header{left:973px;top:66px;width:128px;height:42px;background:var(--green-dark)}

/* nav */
.main-nav{left:99px;top:146px;width:1002px;height:37px;background:var(--white);display:flex;align-items:center;padding-left:16px;gap:26px;z-index:2}
.main-nav a{font-size:11px;font-weight:600;color:var(--ink);text-decoration:none;display:flex;align-items:center;gap:18px}
.main-nav a::after{content:"";border-left:4px solid transparent;border-right:4px solid transparent;border-top:5px solid var(--ink)}
.main-nav a:last-child::after{margin-left:0}

/* hero */
.hero{left:0;top:161px;width:1200px;height:650px;background:linear-gradient(180deg,#1f6fb4 0%,#2c7fc0 35%,#3d6c92 60%,#b4572a 82%,#3a2212 100%)}
.hero-title{left:97px;top:326px;font-family:"Raleway",sans-serif;font-weight:500;font-size:38px;line-height:42px;color:var(--white);width:600px}
.hero-text{left:97px;top:434px;width:540px;font-family:"Raleway",sans-serif;font-size:12px;line-height:18px;color:var(--white)}
.btn-hero{left:97px;top:502px;width:129px;height:41px;background:var(--green);font-size:13px}

/* features */
.features{left:84px;top:681px;width:1031px;height:227px;background:var(--white);padding:13px 15px;display:flex;gap:26px}
.feature{width:313px;height:212px;background:var(--panel);border:1px solid var(--border);padding:22px 24px}
.feature:nth-child(3){margin-left:3px}
.feature svg{width:34px;height:40px;display:block}
.feature h3{margin-top:32px;font-size:14px;font-weight:700;color:var(--ink)}
.feature p{margin-top:14px;font-size:13px;line-height:21px;color:#444}

/* section headings */
.section-title{left:0;width:1200px;text-align:center;font-size:30px;font-weight:700;color:var(--ink)}
.rule{left:558px;width:84px;height:2px;background:var(--green-line)}
.section-sub{left:0;width:1200px;text-align:center;font-size:20px;font-weight:400;color:var(--green);text-transform:uppercase}

/* about */
.about-text{left:130px;top:1076px;width:940px;text-align:center;font-size:15px;line-height:21px;color:var(--text)}
.btn-about{left:537px;top:1167px;width:128px;height:41px;background:var(--green);font-size:13px}

/* services */
.services{left:0;top:1254px;width:1200px;height:568px;background:linear-gradient(90deg,#dcdcdc 0%,#f1f1f1 30%,#f4f4f4 70%,#dedede 100%)}
.service-photo{left:447px;top:1395px;width:302px;height:427px;background:radial-gradient(ellipse at 50% 40%,#e9d2be 0%,#cfb69c 40%,#efefef 75%,rgba(240,240,240,0) 100%)}
.service{width:300px}
.service h4{font-size:15px;font-weight:600;color:var(--ink);text-transform:uppercase}
.service p{margin-top:6px;font-size:12px;line-height:20px;color:#444}
.service.left{left:27px;text-align:right}
.service.right{left:840px}
.svc-icon{width:62px;height:62px;border-radius:50%;display:flex;align-items:center;justify-content:center}
.svc-icon.dark{background:var(--green-dark)}
.svc-icon.light{background:var(--green)}
.svc-icon svg{width:26px;height:26px}

/* booking form */
.field{height:39px;border:1px solid var(--border);background:var(--white);font-family:"Raleway",sans-serif;font-size:12px;color:#555;padding:0 13px;display:flex;align-items:center;justify-content:space-between}
.field.full{left:247px;width:694px}
.field.half-l{left:247px;width:315px}
.field.half-r{left:626px;width:315px}
.field.area{align-items:flex-start;padding-top:12px;height:142px}
.chev{width:8px;height:8px;border-right:1.5px solid var(--green);border-bottom:1.5px solid var(--green);transform:rotate(45deg);margin-top:-4px}
.btn-send{left:830px;top:2435px;width:111px;height:43px;background:var(--green);font-size:12px;gap:8px}

/* footer */
.footer{left:0;top:2622px;width:1200px;height:295px;background:var(--green-dark)}
.footer-badge{left:490px;top:2530px;width:182px;height:182px;border-radius:50%;background:var(--white);display:flex;align-items:center;justify-content:center;text-align:center}
.footer-badge span{font-weight:700;font-size:19px;line-height:1.2;color:var(--green-dark)}
.footer-nav{left:0;top:2741px;width:1200px;display:flex;justify-content:center;gap:12px;font-size:12px;font-weight:600;color:var(--white)}
.footer-nav span.sep{opacity:.9}
.copyright{left:0;top:2774px;width:1200px;text-align:center;font-family:"Raleway",sans-serif;font-size:13px;font-weight:600;color:var(--white)}
.footer-social{left:0;top:2818px;width:1200px;display:flex;justify-content:center;gap:14px}
.footer-social span{width:26px;height:26px;background:#0a4f29;transform:rotate(45deg)}
</style>
</head>
<body>

<div class="abs top-strip"></div>
<div class="abs social-top"><span></span><span></span><span></span><span></span></div>

<header>
  <div class="abs brand"><div class="brand-mark"></div><div class="brand-name">Maple Ridge<br>Solutions</div></div>

  <div class="abs contact email">
    <svg viewBox="0 0 26 26"><rect x="2" y="5" width="22" height="16" rx="1" fill="none" stroke="#6bbd4a" stroke-width="2"/><path d="M2 6l11 8 11-8" fill="none" stroke="#6bbd4a" stroke-width="2"/></svg>
    <div><small>Email Support</small><b>info@mapleridgesolutions.com</b></div>
  </div>
  <div class="abs contact call">
    <svg viewBox="0 0 26 26"><path d="M6 3l4 1 2 5-3 2c1 3 3 5 6 6l2-3 5 2 1 4c-1 2-3 3-5 3C10 22 4 16 3 8c0-2 1-4 3-5z" fill="#6bbd4a"/></svg>
    <div><small>Call Support</small><b>+973 1700 5820</b></div>
  </div>
  <div class="abs btn btn-header">Get a quote</div>
</header>

<section class="abs hero" role="img" aria-label="City skyline at dusk with twin sail-shaped towers and glowing streets"></section>

<nav class="abs main-nav">
  <a>HOME</a><a>ABOUT US</a><a>SERVICES</a><a>PAGES</a><a>PROJECTS</a><a>NEWS</a><a>CONTACT</a>
</nav>

<h1 class="abs hero-title">High quality cleaning services &amp; affordable price</h1>
<p class="abs hero-text">Lorem ipsum dolor sit amet conse ctetur adipisicing elit, sed do eiusmod tempor incididunt ut labore et dolore magna aliqua. Ut enim ad minim veniam</p>
<div class="abs btn btn-hero">Get a quote</div>

<section class="abs features">
  <div class="feature">
    <svg viewBox="0 0 34 40"><rect x="5" y="3" width="24" height="34" fill="none" stroke="#9bcb3b" stroke-width="2.5"/><g fill="#9bcb3b"><rect x="10" y="9" width="4" height="4"/><rect x="20" y="9" width="4" height="4"/><rect x="10" y="17" width="4" height="4"/><rect x="20" y="17" width="4" height="4"/><rect x="14" y="27" width="6" height="10"/></g></svg>
    <h3>GLOBAL LOCATIONS</h3>
    <p>Lorem ipsum dolor sit amet, consectetur adipisicing elit sed do eiusmod tempor.</p>
  </div>
  <div class="feature">
    <svg viewBox="0 0 34 40"><g fill="#9bcb3b"><ellipse cx="17" cy="9" rx="14" ry="5"/><path d="M3 14c0 3 6 5 14 5s14-2 14-5v6c0 3-6 5-14 5S3 23 3 20z"/><path d="M3 25c0 3 6 5 14 5s14-2 14-5v6c0 3-6 5-14 5S3 34 3 31z"/></g></svg>
    <h3>ANYTIME SUPPORT</h3>
    <p>Lorem ipsum dolor sit amet, consectetur adipisicing elit sed do eiusmod tempor.</p>
  </div>
  <div class="feature">
    <svg viewBox="0 0 34 40"><rect x="3" y="7" width="28" height="28" fill="none" stroke="#9bcb3b" stroke-width="2.5"/><rect x="3" y="7" width="28" height="7" fill="#9bcb3b"/><rect x="9" y="3" width="3" height="8" fill="#9bcb3b"/><rect x="22" y="3" width="3" height="8" fill="#9bcb3b"/></svg>
    <h3>SPEND EFFICIENTLY</h3>
    <p>Lorem ipsum dolor sit amet, consectetur adipisicing elit sed do eiusmod tempor.</p>
  </div>
</section>

<!-- About -->
<h2 class="abs section-title" style="top:960px">ABOUT US</h2>
<div class="abs rule" style="top:1006px"></div>
<p class="abs section-sub" style="top:1032px">The best team is here in your city</p>
<p class="abs about-text">Lorem ipsum dolor sit amet conse ctetur adipisicing elit, sed do eiusmod tempor incididunt ut labore et dolore magna aliqua. Ut enim ad minim veniam, quis nostrud exercitation ullamco laboris nisi ut aliquip ex ea commodo consequat. Duis aute irure<br>dolor in reprehenderit in voluptate velit esse cillum dolore eu fugiat nulla pariatur.</p>
<div class="abs btn btn-about">Read more</div>

<!-- Services -->
<section class="abs services"></section>
<h2 class="abs section-title" style="top:1295px">OUR SERVICES</h2>
<div class="abs rule" style="top:1340px"></div>
<p class="abs section-sub" style="top:1367px">Get satisfied with the services we provide A to Z in cleaning</p>
<div class="abs service-photo" role="img" aria-label="Smiling cleaner giving an OK hand sign"></div>

<div class="abs service left" style="top:1427px"><h4>Office Cleaning</h4><p>Lorem ipsum dolor sit amet, consecte-<br>tur adipiscing elit, sed do eiusmod</p></div>
<div class="abs service left" style="top:1541px"><h4>Home Cleaning</h4><p>Lorem ipsum dolor sit amet, consecte-<br>tur adipiscing elit, sed do eiusmod</p></div>
<div class="abs service left" style="top:1654px"><h4>Upholsery Cleaning</h4><p>Lorem ipsum dolor sit amet, consecte-<br>tur adipiscing elit, sed do eiusmod</p></div>

<div class="abs service right" style="top:1427px"><h4>Commercial Cleaning</h4><p>Lorem ipsum dolor sit amet, consecte-<br>tur adipiscing elit, sed do eiusmod</p></div>
<div class="abs service right" style="top:1541px"><h4>Apartment Cleaning</h4><p>Lorem ipsum dolor sit amet, consecte-<br>tur adipiscing elit, sed do eiusmod</p></div>
<div class="abs service right" style="top:1654px"><h4>Window Washing</h4><p>Lorem ipsum dolor sit amet, consecte-<br>tur adipiscing elit, sed do eiusmod</p></div>

<div class="abs svc-icon dark" style="left:344px;top:1428px"><svg viewBox="0 0 26 26"><rect x="6" y="7" width="14" height="16" rx="1" fill="#fff"/><rect x="4" y="4" width="18" height="2" fill="#fff"/><g stroke="#0d6b38" stroke-width="1.5"><line x1="10" y1="10" x2="10" y2="20"/><line x1="13" y1="10" x2="13" y2="20"/><line x1="16" y1="10" x2="16" y2="20"/></g></svg></div>
<div class="abs svc-icon light" style="left:344px;top:1542px"><svg viewBox="0 0 26 26"><path d="M6 8h14l-2 15H8z" fill="#fff"/><rect x="5" y="4" width="16" height="3" fill="#fff"/></svg></div>
<div class="abs svc-icon dark" style="left:344px;top:1655px"><svg viewBox="0 0 26 26"><path d="M7 12h12l-2 11H9z" fill="#fff"/><circle cx="13" cy="7" r="4" fill="none" stroke="#fff" stroke-width="2"/></svg></div>

<div class="abs svc-icon light" style="left:763px;top:1428px"><svg viewBox="0 0 26 26"><rect x="8" y="11" width="11" height="12" rx="2" fill="#fff"/><rect x="10" y="5" width="7" height="5" fill="#fff"/><rect x="4" y="6" width="5" height="2" fill="#fff"/></svg></div>
<div class="abs svc-icon dark" style="left:763px;top:1542px"><svg viewBox="0 0 26 26"><rect x="12" y="2" width="2" height="12" fill="#fff"/><path d="M6 14h14l2 8H4z" fill="#fff"/></svg></div>
<div class="abs svc-icon light" style="left:763px;top:1655px"><svg viewBox="0 0 26 26"><rect x="6" y="4" width="14" height="18" rx="1" fill="#fff"/><circle cx="13" cy="14" r="4" fill="#9bcb3b"/></svg></div>

<!-- Booking -->
<h2 class="abs section-title" style="top:1869px">OUR SERVICES</h2>
<div class="abs rule" style="top:1915px"></div>
<p class="abs section-sub" style="top:1942px">We provide annual service booking</p>

<form>
  <div class="abs field full" style="top:2009px">Full Name</div>
  <div class="abs field half-l" style="top:2062px">Email address</div>
  <div class="abs field half-r" style="top:2062px">Phone number</div>
  <div class="abs field full" style="top:2114px">Address</div>
  <div class="abs field half-l" style="top:2167px">City</div>
  <div class="abs field half-r" style="top:2167px">Zip/Poscode</div>
  <div class="abs field half-l" style="top:2219px">Choose a service<i class="chev"></i></div>
  <div class="abs field half-r" style="top:2219px">Choose a Option<i class="chev"></i></div>
  <div class="abs field full area" style="top:2272px">Your message</div>
  <div class="abs btn btn-send">Send <span>›</span></div>
</form>

<!-- Footer -->
<footer>
  <div class="abs footer"></div>
  <div class="abs footer-badge"><span>Maple Ridge<br>Solutions</span></div>
  <div class="abs footer-nav">
    <span>HOME</span><span class="sep">|</span><span>ABOUT US</span><span class="sep">|</span><span>SERVICES</span><span class="sep">|</span><span>PAGES</span><span class="sep">|</span><span>PROJECTS</span><span class="sep">|</span><span>NEWS</span><span class="sep">|</span><span>CONTACT</span>
  </div>
  <p class="abs copyright">Copyright © 2016.Northwind Studio . All rights reserved</p>
  <div class="abs footer-social"><span></span><span></span><span></span><span></span></div>
</footer>

</body>
</html>
```